Maple Row Yardcare

I want it as prefession and attractive as possible we are a lawnmowing business

Phone number 605-318-2264
Name- Carl Whitby
Email- mapleroweyardsd@fernpost.net

```html
<!DOCTYPE html>
<html lang="en">
<head>
<meta charset="utf-8">
<title>Maple Row Yardcare – Business Cards</title>
<link href="https://fonts.googleapis.com/css2?family=Exo+2:wght@700&family=Montserrat:wght@400&display=swap" rel="stylesheet">
<style>
  :root {
    --backdrop: #1f1f21;
    --forest: #0b5e3a;
    --leaf: #5cbf45;
    --paper: #ffffff;
    --card-w: 520px;
    --card-h: 297px;
  }
  * { box-sizing: border-box; margin: 0; padding: 0; }
  html, body {
    width: 1200px;
    height: 795px;
    overflow: hidden;
    background: var(--backdrop);
  }
  .stage {
    position: relative;
    width: 1200px;
    height: 795px;
  }
  .card {
    position: absolute;
    width: var(--card-w);
    height: var(--card-h);
    overflow: hidden;
    box-shadow: 0 14px 30px rgba(0,0,0,.45);
  }

  /* Back of card */
  .card-back {
    left: 60px;
    top: 110px;
    background: var(--forest);
    display: flex;
    align-items: center;
    justify-content: center;
  }
  .wordmark {
    display: flex;
    align-items: center;
    gap: 12px;
    font-family: "Exo 2", sans-serif;
    font-weight: 700;
    text-transform: uppercase;
    letter-spacing: .02em;
    line-height: 1;
  }
  .wordmark-dot {
    width: 18px;
    height: 18px;
    border-radius: 50%;
    flex: none;
  }
  .card-back .wordmark { color: var(--leaf); font-size: 34px; }
  .card-back .wordmark-dot { background: var(--leaf); }

  /* Front of card */
  .card-front {
    left: 620px;
    top: 388px;
    background: var(--forest);
  }
  .front-top-strip {
    height: 10px;
    background: var(--forest);
  }
  .front-brand-band {
    height: 128px;
    background: var(--paper);
    display: flex;
    align-items: center;
    justify-content: center;
  }
  .card-front .wordmark { color: var(--forest); font-size: 34px; }
  .card-front .wordmark-dot { background: var(--forest); }

  .holder-name {
    position: absolute;
    top: 162px;
    left: 0;
    width: 100%;
    text-align: center;
    font-family: "Exo 2", sans-serif;
    font-weight: 700;
    font-size: 28px;
    letter-spacing: .05em;
    text-transform: uppercase;
    color: var(--paper);
  }
  .contact {
    position: absolute;
    display: flex;
    align-items: center;
    gap: 9px;
    font-family: "Montserrat", sans-serif;
    font-size: 12.5px;
    color: var(--paper);
  }
  .contact svg { width: 16px; height: 16px; flex: none; }
  .contact-phone { left: 26px; bottom: 58px; }
  .contact-email { right: 24px; bottom: 22px; }
</style>
</head>
<body>
<main class="stage">

  <section class="card card-back" aria-label="Business card back">
    <div class="wordmark">
      <span class="wordmark-dot"></span>
      <span class="wordmark-name">Maple Row Yardcare</span>
    </div>
  </section>

  <section class="card card-front" aria-label="Business card front">
    <div class="front-top-strip"></div>
    <div class="front-brand-band">
      <div class="wordmark">
        <span class="wordmark-dot"></span>
        <span class="wordmark-name">Maple Row Yardcare</span>
      </div>
    </div>

    <h1 class="holder-name">Carl Whitby</h1>

    <p class="contact contact-phone">
      <svg viewBox="0 0 16 16" aria-hidden="true">
        <circle cx="8" cy="8" r="8" fill="#ffffff"/>
        <path d="M5.6 4.2l1.3 1.6-.7 1c.5 1.1 1.3 1.9 2.4 2.4l1-.7 1.6 1.3-.8 1.3c-2.9-.3-5.3-2.7-5.6-5.6z" fill="#0b5e3a"/>
      </svg>
      <span>605-318-2264</span>
    </p>

    <p class="contact contact-email">
      <svg viewBox="0 0 16 16" aria-hidden="true">
        <circle cx="8" cy="8" r="8" fill="#ffffff"/>
        <text x="8" y="11.5" text-anchor="middle" font-family="Montserrat, sans-serif" font-size="10" fill="#0b5e3a">@</text>
      </svg>
      <span>mapleroweyardsd@fernpost.net</span>
    </p>
  </section>

</main>
</body>
</html>
```